Statement of Professional Excellence

Our school community has create a statement of Professional Excellence at our school (LAM = The Linden Academy at Marbury) This will be shared internally and with candidates interviewing at our school. We'd like a branded graphic that lists in an interesting way our statements:

Professional Excellence at LAM

We honor the whole child while embracing them where they are.
We are mission-driven individuals whose dedication to our students motivates our daily work.
We bring flexible thinking to allow the needs of the students to drive the learning.
We are patient, nurturing, empathetic, and compassionate people.
We value, trust, and support each other.
We learn and we teach.
We lean into and celebrate diversity.
We build trust through genuine partnerships with families.
We are quirky, fun and proud of it.

```html
<!DOCTYPE html>
<html lang="en">
<head>
<meta charset="utf-8">
<title>Professional Excellence – The Linden Academy at Marbury</title>
<link rel="stylesheet" href="https://fonts.googleapis.com/css2?family=Lora:ital,wght@0,700;1,700&display=swap">
<style>
  :root {
    --gold: #dcbe38;
    --gold-soft: #e8d27a;
    --cream: #f5ecc8;
    --white: #ffffff;
    --navy: #1d3550;
    --green: #1f4a2a;
    --line-light: rgba(250, 236, 180, 0.75);
  }
  html, body {
    margin: 0;
    padding: 0;
    overflow: hidden;
  }
  .poster {
    position: relative;
    width: 927px;
    height: 1200px;
    overflow: hidden;
    background: linear-gradient(90deg,
      var(--gold) 0%,
      var(--gold-soft) 14%,
      var(--cream) 30%,
      var(--white) 44%,
      var(--white) 56%,
      var(--cream) 70%,
      var(--gold-soft) 86%,
      var(--gold) 100%);
  }
  .poster__curves {
    position: absolute;
    inset: 0;
  }
  .poster__content {
    position: relative;
    text-align: center;
  }
  .poster__title {
    margin: 0;
    padding-top: 96px;
    font-family: "Lora", Georgia, serif;
    font-weight: 700;
    font-size: 32px;
    letter-spacing: 0.5px;
    color: var(--navy);
  }
  .statements {
    list-style: none;
    margin: 64px auto 0;
    padding: 0;
    width: 600px;
    font-family: "Lora", Georgia, serif;
    font-style: italic;
    font-weight: 700;
    font-size: 20.5px;
    line-height: 27.4px;
    color: var(--green);
  }
  .statements li {
    margin-bottom: 27.4px;
  }
  .school-name {
    position: absolute;
    left: 0;
    right: 0;
    top: 1000px;
    margin: 0;
    font-family: "Lora", Georgia, serif;
    font-weight: 700;
    font-size: 34px;
    line-height: 44px;
    color: var(--navy);
    text-align: center;
  }
</style>
</head>
<body>
<main class="poster">
  <svg class="poster__curves" width="927" height="1200" viewBox="0 0 927 1200" aria-hidden="true">
    <g fill="none" stroke="var(--line-light)" stroke-width="3">
      <path d="M40 0 C 120 300, 120 900, 40 1200"/>
      <path d="M0 120 C 60 400, 60 800, 0 1080"/>
      <path d="M887 0 C 807 300, 807 900, 887 1200"/>
      <path d="M927 120 C 867 400, 867 800, 927 1080"/>
    </g>
    <g fill="none" stroke="rgba(190,170,90,0.45)" stroke-width="4">
      <path d="M62 0 C 135 300, 135 900, 62 1200"/>
      <path d="M865 0 C 792 300, 792 900, 865 1200"/>
    </g>
  </svg>

  <div class="poster__content">
    <h1 class="poster__title">PROFESSIONAL EXCELLENCE</h1>
    <ul class="statements">
      <li>We honor<br>the whole child while embracing them where they are.</li>
      <li>We are mission-driven<br>individuals whose dedication to our students<br>motivates our daily work.</li>
      <li>We bring flexible<br>thinking to allow the needs of the students<br>to drive the learning.</li>
      <li>We are patient, nurturing,<br>empathetic, and compassionate<br>people.</li>
      <li>We value, trust, and support<br>each other.</li>
      <li>We learn and we teach.</li>
      <li>We lean into and celebrate diversity.</li>
      <li>We build trust through genuine partnerships<br>with families.</li>
      <li>We are quirky, fun and proud of it.</li>
    </ul>
  </div>

  <p class="school-name">The Linden Academy<br>at Marbury</p>
</main>
</body>
</html>
```